Business Card for QRB Farmstock

Custom Business Card Brief:
1. We need two designs for this single client, QRB Farmstock LLC and both designs will end up with rounded corner printed cards that fit the PRINTLY.com design format for their special printing style.
2. My client needs two separate card designs since half of their target market is for farm owners in the Cattle and Beef world. The other half of their target market is working with Equine aka Horse farm owners.
3. The look for two card designs can be similar to ensure branding consistency but we will need some space sizing differences so the cards stand out differently in regards to how the services mentioned are laid out on the front of each card design.
4. Both card designs require the front of the card holding all of the great design work. The back of these 2-sided cards will remain white and can just have the contact information listed "again" on the back to match the contact information provided on the front.
5. Card Design 1 will be for Equine customers, Card Design 2 will be for his Cattle/Beef customers.
6. Card Design 1 (Equine) we are thinking we set aside 70% of the card to be dedicated to the Services listed section while the remaining 30% of the front of the card space will hold a smaller logo image space along with his name and contact information.
7. Card Design 2 (Cattle/Beef) we will need opposite of my last point. We want 70% of the card dedicated to a larger logo space and his contact information while the remaining 30% listing the services provided.
8. Card Design #1 - Equine - his Services space should include:
- Equine Mortality Services
- General Removal
- Cremation
- Transportation for Necropsy
9. Card Design #2 - Cattle/Beef - his Services space should include: General Livestock Services, Hauling, Order Buying, Dealing, Dead Stock Removal
10. Contact Information for both card designs:
- Gerald R. Fenwick (owner)
- QRB Farmstock LLC (company)
- 555-318-4692 (phone)
- info@qrbfarmstockservices.example (email)
- QRBFarmstockServices.example (website)
11. Additional Branding Details - The color codes aka pantone colors that are in the current logo file design:
- Blue Pantone 7686C
- Grey Pantone 422C
12. The font styles used in the logo:
- Nexa Bold
- Nexa Rust Slab Black Shadow
13. Back of both card designs, just list his contact information in larger size to stand out more on the white back:
- 555-318-4692 (phone)
Updates

Okay thanks for confirming that our final design files will be ready for the PRINTLY.com format. I noticed the 2nd place vertical card already had rounded corners but the horizontal design that was in 1st place still had sharp square corners. When using the PRINTLY.com format we will be rounding all of the corners of both cards for print. So we just wanted to make sure that both sets of files will be in a rounded design meeting their format sizing to ensure no content from your great designs gets cut off. Thank you again for your attention to detail. ~ Derek

Target Market(s)

Business to Business

Industry/Entity Type

Farming, Agriculture, Livestock

Contact Information for Business Card

Clients' logo, his contact info, and his different services on two similar final card designs.

Font styles to use
Other font styles liked:
• Look at the brief to see how his logo fonts are currently.

Requirements
Must have
• Two versions of the card, one for the Equine horse market, and one for the Cattle/Beef market of farming.
Nice to have
• Clean, sharp, concise.
Should not have
• No flashy or cartoony designs.

```html
<!DOCTYPE html>
<html lang="en">
<head>
<meta charset="utf-8">
<title>QRB Farmstock Business Cards</title>
<link rel="stylesheet" href="https://fonts.googleapis.com/css2?family=Lexend:wght@500;600&display=swap">
<style>
  :root {
    --brand-blue: #1f4f8f;
    --ink: #111111;
    --paper: #ffffff;
    --backdrop: #ffffff;
    --shadow: rgba(0, 0, 0, 0.35);
  }
  * { margin: 0; padding: 0; box-sizing: border-box; }
  html, body {
    width: 1200px; height: 901px; overflow: hidden;
    background: var(--backdrop);
    font-family: "Lexend", "Helvetica Neue", Arial, sans-serif;
  }
  .canvas { position: relative; width: 1200px; height: 901px; }
  .card {
    position: absolute; top: 115px; width: 439px; height: 670px;
    background: var(--paper); border-radius: 34px; overflow: hidden;
    box-shadow: 0 4px 22px var(--shadow);
  }
  .card--equine { left: 120px; }
  .card--cattle { left: 641px; }
  .wordmark {
    position: absolute; left: 0; right: 0; text-align: center;
    color: var(--brand-blue); font-weight: 600; white-space: nowrap;
    display: flex; align-items: center; justify-content: center;
  }
  .card--equine .wordmark { top: 70px; height: 80px; font-size: 40px; }
  .card--cattle .wordmark { top: 80px; height: 100px; font-size: 48px; }
  .owner-name {
    position: absolute; left: 0; right: 0; text-align: center;
    color: var(--ink); font-weight: 600; white-space: nowrap; letter-spacing: -0.3px;
  }
  .card--equine .owner-name { top: 173px; font-size: 33px; }
  .card--cattle .owner-name { top: 223px; font-size: 31px; }
  .services {
    position: absolute; left: 0; right: 0; background: var(--brand-blue);
    color: var(--paper); list-style: none; font-weight: 500;
  }
  .services li::before { content: "- "; }
  .card--equine .services {
    top: 240px; height: 290px; padding: 75px 0 0 36px;
    font-size: 24px; line-height: 32.5px;
  }
  .card--cattle .services {
    top: 307px; height: 189px; padding: 17px 0 0 50px;
    font-size: 24px; line-height: 31.3px;
  }
  .contact {
    position: absolute; left: 0; right: 0; text-align: center;
    color: var(--ink); font-weight: 500; font-style: normal; white-space: nowrap;
  }
  .card--equine .contact { top: 543px; font-size: 17.5px; line-height: 24.3px; }
  .card--cattle .contact { top: 514px; font-size: 21px; line-height: 31.5px; }
  .card--cattle .contact .phone { font-size: 25px; }
</style>
</head>
<body>
<main class="canvas">
  <section class="card card--equine" aria-label="Equine services card">
    <div class="wordmark">QRB Farmstock</div>
    <h1 class="owner-name">Gerald R. Fenwick</h1>
    <ul class="services">
      <li>Equine Mortality Services</li>
      <li>General Removal</li>
      <li>Cremation</li>
      <li>Transportation for Necropsy</li>
    </ul>
    <address class="contact">
      <div>QRB Farmstock LLC</div>
      <div class="phone">555-318-4692</div>
      <div>info@qrbfarmstockservices.example</div>
      <div>QRBFarmstockServices.example</div>
    </address>
  </section>

  <section class="card card--cattle" aria-label="Cattle and beef services card">
    <div class="wordmark">QRB Farmstock</div>
    <h1 class="owner-name">Gerald R. Fenwick</h1>
    <ul class="services">
      <li>General Livestock Services</li>
      <li>Hauling</li>
      <li>Order Buying</li>
      <li>Dealing</li>
      <li>Dead Stock Removal</li>
    </ul>
    <address class="contact">
      <div>QRB Farmstock LLC</div>
      <div class="phone">555-318-4692</div>
      <div>info@qrbfarmstockservices.example</div>
      <div>QRBFarmstockServices.example</div>
    </address>
  </section>
</main>
</body>
</html>
```